Business Telephone Service Brochure

I need a brochure designed to help sell our VoIP service. The brochure needs to be clean, attention getting, professional and have 3 key areas of information (Key Features, Benefits & Service Plans). Here is an idea of what we are looking for https://www.artflockly.com/design/52930487. Need to also include how much the customer could save. See this for an example https://42mockups.com/postcard-flyer-design/contests/voip-sales-flyer-template-replicate-attached-358209. The Service Plan section needs to allow room for two types of plans. One plan includes the phone and has a 12, 24 and 36 month option. Each term (12,24,36) will have its own monthly cost per device. The second service option is no-commitment monthly with a single per month price per device. The included features section should allow for up to 16 features to be listed. The benefits should allow for 4-6 benefits to be listed. Also include room for Logo, business address, website, phone number and email.

Target Market(s)

Small to medium business with 1-100 employees.

Industry/Entity Type

Telecommunications

Font styles to use
Serif

Colors

Designer to choose colors to be used in the design.

Requirements
Must have
• Key Feature, Benefits and Service Plans (i.e. Pricing). Company logo, phone, email and website. Must have "Save up to x%!" and catch attention.
Nice to have
• Limited colors. I am not setting a hard limit, please take the liberty to do what you feel is needed. Just keep in mind we want it to be clean, professional and attention getting without being to flashy or obnoxious.
Should not have
• Nothing busy or distracting.

```html
<!DOCTYPE html>
<html lang="en">
<head>
<meta charset="utf-8">
<title>nexlo — Business Telephone Service Flyer</title>
<link rel="stylesheet" href="https://fonts.googleapis.com/css2?family=Roboto:wght@400;500;700&family=Roboto+Condensed:wght@700&family=Montserrat:wght@400&display=swap">
<style>
  :root{
    --board:#464646;
    --ink-purple:#2c2466;
    --slate:#6c7075;
    --paper:#ffffff;
    --row:#f1f1f1;
    --row-alt:#e9e9e9;
    --text-dark:#222;
    --rule:#bdbdc8;
  }
  *{box-sizing:border-box;margin:0;padding:0}
  html,body{width:1200px;height:1200px;overflow:hidden;background:var(--board);font-family:"Roboto",Arial,sans-serif}
  .board{position:relative;width:1200px;height:1200px}
  .side-label{position:absolute;top:124px;width:200px;margin-left:-100px;text-align:center;color:#fff;font-family:"Montserrat",sans-serif;font-size:26px;letter-spacing:1px}
  .flyer{position:absolute;background:var(--paper);overflow:hidden}
  .flyer svg.shapes{position:absolute;left:0;top:0}
  .front{left:30px;top:178px;width:550px;height:776px}
  .back{left:613px;top:174px;width:555px;height:785px}
  .abs{position:absolute}
  .brand{font-family:"Roboto",sans-serif;font-weight:700;color:var(--ink-purple);font-size:42px;letter-spacing:-1px;line-height:1;white-space:nowrap}
  .brand-tag{font-size:6px;color:var(--ink-purple);letter-spacing:.1px;margin-top:3px;white-space:nowrap}
  .front-logo{right:18px;top:20px;text-align:right}
  .section-head{font-family:"Roboto Condensed",sans-serif;font-weight:700;color:#fff;letter-spacing:3px;font-size:18px;display:flex;align-items:center;gap:8px}
  .features{list-style:none;left:32px;top:445px}
  .features li{display:flex;align-items:center;height:20.6px;font-size:9px;color:var(--text-dark)}
  .features .dot{width:16px;height:16px;border-radius:50%;background:var(--ink-purple);margin-right:8px;flex:none;display:flex;align-items:center;justify-content:center}
  .features .dot i{width:6px;height:6px;border-radius:50%;border:1.5px solid #fff}
  .benefits{list-style:none;left:302px;top:446px;width:242px}
  .benefits li{height:31px;display:flex;align-items:center;font-size:10.8px;color:var(--ink-purple);border-bottom:1px dotted var(--rule)}
  .benefits li:last-child{border-bottom:none}
  .save-callout{left:302px;top:648px;font-family:"Roboto",sans-serif;font-weight:700;font-size:21px;color:var(--ink-purple);white-space:nowrap}
  .contact{color:#fff;font-size:10px;display:flex;align-items:center;gap:5px;white-space:nowrap}
  .pricing-table{position:absolute;left:29px;top:460px;width:499px;border-collapse:separate;border-spacing:1px 0;font-family:"Roboto",sans-serif}
  .pricing-table th{height:58px;color:#fff;font-weight:700;font-size:13.5px;line-height:1;background:var(--ink-purple)}
  .pricing-table th.service-col{background:var(--slate);font-size:15px;width:177px}
  .pricing-table td{text-align:center;font-size:7.5px;color:var(--text-dark);background:var(--row);height:41px}
  .pricing-table td.price{font-weight:700;font-size:8.5px}
  .pricing-table tr.alt td{background:var(--row-alt)}
  .notes{left:34px;top:618px;font-size:8.5px;color:var(--ink-purple);line-height:21px;list-style:none}
  .notes li::before{content:"• ";color:#888}
  .back-logo{left:22px;top:702px}
  .back-contacts{right:24px;top:726px;text-align:right}
  .back-contacts .contact{justify-content:flex-end;letter-spacing:2px;height:16.5px;font-size:9.5px}
</style>
</head>
<body>
<div class="board">
  <div class="side-label" style="left:326px">FRONT</div>
  <div class="side-label" style="left:895px">BACK</div>

  <!-- FRONT -->
  <section class="flyer front">
    <svg class="shapes" width="550" height="776" viewBox="0 0 550 776">
      <defs>
        <linearGradient id="officeTones" x1="0" y1="0" x2="1" y2="1">
          <stop offset="0" stop-color="#dfe3e6"/>
          <stop offset=".45" stop-color="#c9c2b6"/>
          <stop offset=".75" stop-color="#e6b357"/>
          <stop offset="1" stop-color="#eeeae4"/>
        </linearGradient>
      </defs>
      <rect role="img" aria-label="Photo of a smiling support agent wearing a headset at a desk, with colleagues working at computers behind her" x="0" y="0" width="550" height="432" fill="url(#officeTones)"/>
      <polygon points="550,300 326,399 550,446" fill="var(--slate)"/>
      <polygon points="0,363 406,363 326,399 0,399" fill="var(--ink-purple)"/>
      <polygon points="0,716 286,758 262,776 0,776" fill="var(--slate)"/>
      <polygon points="262,776 550,636 550,776" fill="var(--ink-purple)"/>
    </svg>

    <div class="abs front-logo">
      <div class="brand">nexlo</div>
      <div class="brand-tag">Internet-Telephone-Security-Networking</div>
    </div>

    <div class="abs section-head" style="left:24px;top:369px">
      <svg width="16" height="20" viewBox="0 0 16 20"><rect x="1" y="3" width="14" height="16" rx="1.5" fill="#fff"/><rect x="5" y="1" width="6" height="4" rx="1" fill="#fff" stroke="var(--ink-purple)"/><path d="M4 10l2 2 3-4" stroke="var(--ink-purple)" stroke-width="1.5" fill="none"/><rect x="10" y="10" width="3" height="1.5" fill="var(--ink-purple)"/><rect x="4" y="15" width="9" height="1.5" fill="var(--ink-purple)"/></svg>
      KEY FEATURES
    </div>
    <div class="abs section-head" style="left:392px;top:378px">
      <svg width="22" height="22" viewBox="0 0 22 22"><rect x="1" y="9" width="5" height="12" fill="#fff"/><path d="M7 10l5-8c2 0 2 2 1.5 5H20c1.2 0 2 1 1.6 2.2l-2.4 9.5c-.3 1-1 1.3-2 1.3H7z" fill="#fff"/></svg>
      BENEFITS
    </div>

    <ul class="abs features">
      <li><span class="dot"><i></i></span>Unlimited local and long distance calling</li>
      <li><span class="dot"><i></i></span>HD Voice</li>
      <li><span class="dot"><i></i></span>Business SMS/Text Messaging</li>
      <li><span class="dot"><i></i></span>Personal and Shared Voice mail Boxes</li>
      <li><span class="dot"><i></i></span>Audio Conferencing</li>
      <li><span class="dot"><i></i></span>Intercom</li>
      <li><span class="dot"><i></i></span>Mobile App</li>
      <li><span class="dot"><i></i></span>Auto Attendant/Interactive Voice Routing</li>
      <li><span class="dot"><i></i></span>Free web or email fax</li>
      <li><span class="dot"><i></i></span>Web admin portal</li>
      <li><span class="dot"><i></i></span>Music On Hold - Customizable</li>
      <li><span class="dot"><i></i></span>Simultaneous ring / follow-me</li>
      <li><span class="dot"><i></i></span>Redundancy/Failover – Never miss a call</li>
    </ul>

    <ul class="abs benefits">
      <li>No expensive onsite telephone equipment</li>
      <li>Easily scale up or down and needs change</li>
      <li>Free telephone/email support</li>
      <li>Lower monthly cost</li>
      <li>Increase reliability</li>
      <li>Easy self-administration</li>
    </ul>

    <div class="abs save-callout">Save up to x%!</div>

    <div class="abs contact" style="left:410px;top:726px;font-size:11px">
      <svg width="11" height="11" viewBox="0 0 12 12"><circle cx="6" cy="6" r="5" fill="none" stroke="#fff"/><ellipse cx="6" cy="6" rx="2.2" ry="5" fill="none" stroke="#fff"/><line x1="1" y1="6" x2="11" y2="6" stroke="#fff"/></svg>
      Company website
    </div>
  </section>

  <!-- BACK -->
  <section class="flyer back">
    <svg class="shapes" width="555" height="785" viewBox="0 0 555 785">
      <defs>
        <linearGradient id="deskTones" x1="0" y1="0" x2="1" y2="1">
          <stop offset="0" stop-color="#4a4f58"/>
          <stop offset=".4" stop-color="#7b7d84"/>
          <stop offset=".7" stop-color="#a99a86"/>
          <stop offset="1" stop-color="#d9c9b0"/>
        </linearGradient>
      </defs>
      <rect role="img" aria-label="Photo of a headset resting on a desk in front of an office desk phone, softly blurred" x="0" y="0" width="555" height="437" fill="url(#deskTones)"/>
      <polygon points="0,304 223,402 0,452" fill="var(--ink-purple)"/>
      <polygon points="0,654 279,753 359,785 0,785" fill="var(--slate)"/>
      <polygon points="555,683 279,753 359,785 555,785" fill="var(--ink-purple)"/>
    </svg>

    <div class="abs section-head" style="left:32px;top:378px;letter-spacing:0.5px;font-size:19px">$ PRICING</div>

    <table class="pricing-table">
      <thead>
        <tr>
          <th class="service-col">Service</th>
          <th>Monthly</th>
          <th>12 month<br>term</th>
          <th>24 month<br>term</th>
          <th>36 month<br>term</th>
        </tr>
      </thead>
      <tbody>
        <tr>
          <td>Phone service only<br>(phone sold separately)</td>
          <td class="price">$21.95</td>
          <td></td><td></td><td></td>
        </tr>
        <tr class="alt">
          <td>Service + 2 Corvan P20 Phone</td>
          <td></td>
          <td class="price">$24.95</td>
          <td class="price">$22.95</td>
          <td class="price">$20.95</td>
        </tr>
      </tbody>
    </table>

    <ul class="abs notes">
      <li>For monthly service you may purchase the Corvan P20 phone for $65 each, less taxes and shipping.</li>
      <li>Corvan P20 phones are rented and due upon cancellation. Customer pays return shipping</li>
    </ul>

    <div class="abs back-logo">
      <div class="brand" style="color:#fff;font-size:40px">nexlo</div>
      <div class="brand-tag" style="color:#fff;font-size:5px">Internet-Telephone-Security-Networking</div>
    </div>
    <div class="abs contact" style="left:24px;top:756px">
      <svg width="9" height="12" viewBox="0 0 10 13"><path d="M5 0a5 5 0 0 0-5 5c0 3.5 5 8 5 8s5-4.5 5-8a5 5 0 0 0-5-5z" fill="#fff"/><circle cx="5" cy="5" r="1.8" fill="var(--slate)"/></svg>
      Company address
    </div>

    <div class="abs back-contacts">
      <div class="contact"><svg width="10" height="10" viewBox="0 0 12 12"><path d="M2.5 1l2 2.5-1 1.3c.7 1.5 1.8 2.6 3.3 3.3l1.3-1 2.4 2-1.2 1.6C6 10.5 1.5 6 1 2.2z" fill="#fff"/></svg>Company number</div>
      <div class="contact"><svg width="11" height="8" viewBox="0 0 12 8"><rect width="12" height="8" fill="#fff"/><path d="M0 0l6 4.5L12 0" stroke="var(--ink-purple)" fill="none"/></svg>Company email</div>
      <div class="contact"><svg width="10" height="10" viewBox="0 0 12 12"><circle cx="6" cy="6" r="5" fill="none" stroke="#fff"/><ellipse cx="6" cy="6" rx="2.2" ry="5" fill="none" stroke="#fff"/><line x1="1" y1="6" x2="11" y2="6" stroke="#fff"/></svg>Company website</div>
    </div>
  </section>
</div>
</body>
</html>
```